Web Design Project

We need a web design for a new business in Orland Park, IL.
We are a restaurant meal delivery business. We deliver from a variety of restaurants. We gives our customers an alternative to just pizza delivery.

Websites we like:
http://www.quillbarkrunners.com/
https://www.fennowmealpost.com/Default.asp
www.brambletrayhaul.com/

Our current website is www.zestwickdrop.com(not to be used as a guide, i'm looking for an original design)
Updates

Please no pictures of anything associated with Pizza.  We are a restaurant delivery business that gives our customers an alternative to just pizza delivery. 

This is my original logo.  I uploaded the file to the job brief and updated the brief some.

Target Market(s)

Two income households with children.

Industry/Entity Type

Business

Requirements
Must have
• Order Now button,and sliding photographs of food.
Nice to have
• a background other than white(it can be white if it works with the design)
Should not have
• A picture of pizza that cant be changed. It is ok if the photo is apart of sliding photo's, but pizza cant be the main focus of our delivery service.

```html
<!DOCTYPE html>
<html lang="en">
<head>
<meta charset="utf-8">
<title>Zestwick Drop – Restaurant Delivery</title>
<link href="https://fonts.googleapis.com/css2?family=Roboto+Condensed:wght@400;700&family=Arimo:wght@400&display=swap" rel="stylesheet">
<style>
  :root{
    --red:#cc0f2d;
    --red-dark:#b00c26;
    --white:#ffffff;
    --grey-band:#ecebea;
    --footer-bg:#efeeec;
    --text:#444444;
    --muted:#666666;
    --rule:#dddddd;
    --head:"Roboto Condensed", sans-serif;
    --body:"Arimo", sans-serif;
  }
  *{box-sizing:border-box;margin:0;padding:0}
  html,body{width:1166px;height:1200px;overflow:hidden;background:var(--white)}
  body{position:relative;font-family:var(--body);color:var(--text)}
  .abs{position:absolute}

  /* header */
  .top-band{left:0;top:0;width:1166px;height:44px;background:var(--red)}
  .zigzag{left:0;top:40px;width:1166px;height:8px}
  .main-nav{right:136px;top:13px;display:flex;font-family:var(--head);font-size:13px;color:var(--white)}
  .main-nav span{padding:0 8px;border-left:1px solid rgba(255,255,255,.7);line-height:14px}
  .main-nav span:first-child{border-left:none}
  .brand{left:152px;top:82px;display:flex;align-items:center;gap:8px}
  .brand-dot{width:22px;height:22px;border-radius:50%;background:var(--red)}
  .brand-name{font-family:var(--head);font-weight:700;font-size:34px;color:var(--red);line-height:1}
  .phone{left:662px;top:82px;display:flex;align-items:center;gap:8px;font-family:var(--head);font-size:15px;color:var(--red-dark)}
  .order-now{left:806px;top:70px;width:222px;height:36px}
  .order-now span{position:absolute;inset:0;display:flex;align-items:center;justify-content:center;font-family:var(--head);font-size:17px;color:var(--white)}

  /* slider */
  .slider-band{left:0;top:128px;width:1166px;height:446px;background:radial-gradient(ellipse at center,#f7f7f6 0%,var(--grey-band) 75%)}
  .slider-frame{left:155px;top:161px;width:856px;height:378px;background:var(--white);box-shadow:0 6px 14px rgba(0,0,0,.18)}
  .slide-photo{left:161px;top:168px;width:843px;height:366px;background:linear-gradient(100deg,#e6902a 0%,#f2b24a 35%,#b9641a 60%,#1e140c 100%)}
  .courier-photo{left:660px;top:182px;width:290px;height:392px;background:linear-gradient(180deg,#d7b79b 0%,#2e3b8a 45%,#252f73 100%);border-radius:120px 120px 0 0}
  .slide-arrow{top:457px;width:28px;height:63px;background:var(--red);display:flex;align-items:center;justify-content:center}
  .slide-arrow.prev{left:161px}
  .slide-arrow.next{left:976px}

  /* intro */
  .intro{left:137px;top:595px;width:893px;text-align:center;font-size:11.6px;line-height:15.5px;color:var(--text)}
  .intro p + p{margin-top:22px}
  .intro-rule{left:137px;top:690px;width:893px;height:1px;background:var(--rule)}

  /* feature cards */
  .card{top:728px;width:200px;height:222px;background:linear-gradient(180deg,var(--red) 0%,var(--red-dark) 100%);color:var(--white)}
  .card-icon{position:absolute;left:67px;top:-27px;width:66px;height:66px;border-radius:50%;background:var(--white);box-shadow:0 1px 4px rgba(0,0,0,.25);display:flex;align-items:center;justify-content:center}
  .card h2{position:absolute;left:9px;top:50px;font-family:var(--head);font-weight:400;font-size:17px}
  .field{position:absolute;left:8px;width:174px;height:22px;background:var(--white);border:1px solid #c9c9c9;border-radius:2px;font-size:11.5px;color:var(--text);padding:3px 6px}
  .btn{position:absolute;background:linear-gradient(#ffffff,#e8e8e8);border:1px solid #c8c8c8;border-radius:3px;color:var(--red);display:flex;align-items:center;justify-content:center}
  .card-order{left:137px}
  .card-how{left:367px}
  .card-gift{left:598px}
  .card-login{left:829px}
  .how-text{position:absolute;left:10px;top:80px;width:182px;font-size:11px;line-height:15.5px}
  .gift-art{position:absolute;left:14px;top:78px;width:170px;height:112px;background:linear-gradient(160deg,#f6e6c2 0%,#e9cf94 70%,#c7223a 100%);transform:rotate(4deg);border-radius:3px}
  .gift-caption{position:absolute;left:8px;top:193px;font-family:var(--head);font-size:15px}
  .remember{position:absolute;left:8px;top:142px;display:flex;align-items:center;gap:5px;font-size:11px}
  .remember i{width:11px;height:11px;background:var(--white);border:1px solid #999}
  .create{position:absolute;left:29px;top:193px;font-family:var(--head);font-size:19px;text-decoration:underline}

  /* footer */
  .footer-band{left:0;top:988px;width:1166px;height:172px;background:var(--footer-bg)}
  .foot-col{top:1005px;font-size:11px;line-height:20.6px;color:var(--muted)}
  .foot-divider{top:995px;width:1px;height:162px;background:#d2d2d2}
  .foot-title{font-family:var(--head);font-size:13px;color:#333;margin-bottom:2px}
  .hours li{list-style:none;color:#a8141e}
  .social{left:888px;top:1030px;display:grid;grid-template-columns:repeat(3,28px);gap:10px 11px}
  .social i{display:block;width:28px;height:28px;border-radius:3px}
  .copyright{left:0;top:1175px;width:1166px;text-align:center;font-family:var(--head);font-size:11px;color:#333}
</style>
</head>
<body>

<!-- header -->
<div class="abs top-band"></div>
<svg class="abs zigzag" viewBox="0 0 1166 8" preserveAspectRatio="none" aria-hidden="true">
  <defs><pattern id="zz" width="8" height="8" patternUnits="userSpaceOnUse"><polygon points="0,0 8,0 4,6" fill="#cc0f2d"/></pattern></defs>
  <rect width="1166" height="8" fill="url(#zz)"/>
</svg>
<nav class="abs main-nav">
  <span>Home</span><span>Restaurants</span><span>How do I order?</span><span>Corporate</span><span>Gift Certificate</span><span>About us</span><span>Contact us</span><span>Comments</span>
</nav>
<div class="abs brand"><i class="brand-dot"></i><span class="brand-name">Zestwick Drop</span></div>
<div class="abs phone">
  <svg width="20" height="16" viewBox="0 0 20 16" aria-hidden="true"><path d="M2 6c0-3 4-5 8-5s8 2 8 5l-3 1-1-2H6L5 7z" fill="#cc0f2d"/><rect x="4" y="8" width="12" height="7" rx="2" fill="#cc0f2d"/><circle cx="10" cy="11.5" r="2" fill="#fff"/></svg>
  <span>855-014-2270</span>
</div>
<div class="abs order-now">
  <svg width="222" height="36" viewBox="0 0 222 36" aria-hidden="true">
    <polygon points="0,4 20,4 14,18 20,32 0,32" fill="#b00c26" transform="translate(0,0)"/>
    <polygon points="222,4 202,4 208,18 202,32 222,32" fill="#b00c26"/>
    <rect x="20" y="0" width="182" height="36" fill="#cc0f2d"/>
  </svg>
  <span>ORDER NOW!</span>
</div>

<!-- slider -->
<div class="abs slider-band"></div>
<div class="abs slider-frame"></div>
<div class="abs slide-photo" role="img" aria-label="Close-up of grilled shrimp skewers on a barbecue grill"></div>
<div class="abs courier-photo" role="img" aria-label="Smiling delivery courier in a blue cap and shirt writing an order"></div>
<div class="abs slide-arrow prev"><svg width="10" height="14" viewBox="0 0 10 14"><polygon points="9,0 9,14 0,7" fill="#fff"/></svg></div>
<div class="abs slide-arrow next"><svg width="10" height="14" viewBox="0 0 10 14"><polygon points="1,0 1,14 10,7" fill="#fff"/></svg></div>

<!-- intro -->
<section class="abs intro">
  <p>We really get excited about is delivering culinary delights. Despite the fun name, we take delivery coordination very seriously. As experts in arranging for timely delivery, we coordinate the best food delivery experience for our customers with timely, fresh and professional presentation as our top priorities.</p>
  <p>Whether you’re hosting a party or office meeting, stuck working late in the office, too busy or tired to cook, or can’t stand the thought of eating cereal for dinner yet again, let Zestwick Drop be your dining solution.</p>
</section>
<div class="abs intro-rule"></div>

<!-- cards -->
<section class="abs card card-order">
  <div class="card-icon">
    <svg width="38" height="32" viewBox="0 0 38 32" aria-hidden="true"><path d="M2 3h6l5 18h19l4-13H10" fill="none" stroke="#cc0f2d" stroke-width="3" stroke-linejoin="round"/><circle cx="15" cy="27" r="3" fill="#555"/><circle cx="29" cy="27" r="3" fill="#555"/></svg>
  </div>
  <h2>Ready to Order?</h2>
  <div class="field" style="top:80px">Slect your zip code</div>
  <div style="position:absolute;left:0;top:110px;width:200px;text-align:center;font-size:11.5px">OR</div>
  <div class="field" style="top:130px">Search For Your ZIP Code</div>
  <div class="btn" style="left:104px;top:166px;width:78px;height:25px;font-family:var(--head);font-size:15px">START</div>
</section>

<section class="abs card card-how">
  <div class="card-icon"><span style="font-family:var(--head);font-size:46px;color:#cc0f2d;line-height:1">?</span></div>
  <h2>How</h2>
  <p class="how-text">You can place an order several days or hours in advance or request delivery as soon as possible (usually 45 minutes – 1 hour)</p>
  <div class="btn" style="left:104px;top:171px;width:78px;height:24px;font-size:10.5px">READ MORE...</div>
</section>

<section class="abs card card-gift">
  <div class="card-icon">
    <svg width="28" height="28" viewBox="0 0 28 28" aria-hidden="true"><rect x="3" y="11" width="22" height="15" fill="#7b3fb8"/><rect x="1" y="7" width="26" height="6" fill="#9155cc"/><rect x="12" y="7" width="4" height="19" fill="#3b79d6"/><path d="M14 7c-3-6-9-4-5 0m5 0c3-6 9-4 5 0" fill="none" stroke="#3b79d6" stroke-width="2"/></svg>
  </div>
  <h2>Gift Certificate</h2>
  <div class="gift-art" role="img" aria-label="Gift certificate voucher tied with a red ribbon bow"></div>
  <div class="gift-caption">Gift Certificate Available</div>
</section>

<section class="abs card card-login">
  <div class="card-icon">
    <svg width="26" height="32" viewBox="0 0 26 32" aria-hidden="true"><path d="M6 14V9a7 7 0 0 1 14 0v5" fill="none" stroke="#999" stroke-width="3"/><rect x="2" y="14" width="22" height="17" rx="2" fill="#b5b5b5"/><circle cx="13" cy="22" r="2.5" fill="#555"/></svg>
  </div>
  <h2>Login</h2>
  <div class="field" style="top:79px">Username</div>
  <div class="field" style="top:110px">Password</div>
  <div class="remember"><i></i><span>Remember my email</span></div>
  <div class="btn" style="left:10px;top:158px;width:73px;height:25px;font-family:var(--head);font-size:13px">Login</div>
  <div class="create">CREATE ACCOUNT!</div>
</section>

<!-- footer -->
<div class="abs footer-band"></div>
<ul class="abs foot-col" style="left:137px;list-style:none">
  <li>Home</li><li>Restaurants</li><li>How do I order?</li><li>Corporate account signup</li><li>Gift certificate</li><li>About us</li>
</ul>
<div class="abs foot-divider" style="left:335px"></div>
<ul class="abs foot-col" style="left:402px;list-style:none">
  <li>Contact us</li><li>Comments</li><li>FAQ</li><li>Privacy</li><li>Sitemap</li>
</ul>
<div class="abs foot-divider" style="left:526px"></div>
<div class="abs foot-col" style="left:581px">
  <div class="foot-title">Hours of operation</div>
  <ul class="hours"><li>Monday-Friday : 11AM-2:00PM; 5PM-9:00PM</li><li>Saturday : 5PM-10PM</li><li>Sunday : 5PM-9:00PM</li></ul>
</div>
<div class="abs foot-divider" style="left:845px"></div>
<div class="abs foot-col" style="left:888px"><div class="foot-title">Follow us on</div></div>
<div class="abs social" aria-label="Social links">
  <i style="background:#3a5ca8"></i><i style="background:#2f6fb0"></i><i style="background:#3b5998"></i>
  <i style="background:#2f68c8"></i><i style="background:#1f7ab8"></i><i style="background:#5a7dc0"></i>
  <i style="background:#2e9a4e"></i><i style="background:#3ab4e6"></i><i style="background:#d93a2b"></i>
</div>
<div class="abs copyright">© Tallbirch Studio 2012. All Rights reserved</div>

</body>
</html>
```